Flyer design for webdesign company

create a flyer that can be printed or sent as an email. The flyer needs to be professional, modern and engaging.

Reason: opportunity for all designers to get their designs in.

Target Market(s)

business owners that do not have a website

Industry/Entity Type

It Company

Font styles to use
Sans Serif

```html
<!DOCTYPE html>
<html lang="en">
<head>
<meta charset="utf-8">
<title>Novaweb Studio – Flyer</title>
<link href="https://fonts.googleapis.com/css2?family=Source+Sans+3:wght@400;600;700;800&display=swap" rel="stylesheet">
<style>
  :root {
    --backdrop: #fec45f;
    --paper: #eeeae1;
    --paper-light: #f1ede6;
    --taupe: #c6b9af;
    --taupe-panel: #c9bfb6;
    --ink: #4b4b4b;
    --ink-soft: #5a5a5a;
    --accent: #f39325;
    --white: #ffffff;
    --ghost: rgba(120, 110, 100, 0.12);
  }
  * { box-sizing: border-box; margin: 0; padding: 0; }
  html, body {
    width: 1200px; height: 900px; overflow: hidden;
    background: var(--backdrop);
    font-family: "Source Sans 3", "Myriad Pro", Arial, sans-serif;
  }
  .canvas { position: relative; width: 1200px; height: 900px; }
  .page {
    position: absolute; top: 47px; width: 530px; height: 685px; overflow: hidden;
    box-shadow: 3px 4px 6px rgba(0,0,0,0.25);
  }
  .page--front { left: 60px; background: var(--taupe); }
  .page--back { left: 611px; background: var(--paper); }

  /* front */
  .front__left { position: absolute; left: 0; top: 0; width: 280px; height: 685px; background: var(--paper-light); }
  .front__photo {
    position: absolute; left: 0; top: 362px; width: 530px; height: 323px;
    background: linear-gradient(90deg, #e6e1d9 0%, #ddd6cd 45%, #b9aca2 62%, #a89a90 100%);
  }
  .build-title {
    position: absolute; left: 0; top: 28px; width: 280px; text-align: center;
    color: var(--ink); font-weight: 800; font-size: 31px; line-height: 37.5px;
  }
  .build-title small { display: block; font-size: 12px; line-height: 18px; margin-top: 6px; }
  .brand-front { position: absolute; left: 0; top: 188px; width: 280px; text-align: center; }
  .brand-dot { display: block; margin: 0 auto 22px; width: 96px; height: 96px; border-radius: 50%; background: var(--accent); }
  .brand-name { color: var(--ink); font-weight: 600; font-size: 31px; }

  .headline {
    position: absolute; right: 28px; top: 28px; text-align: right;
    color: var(--white); font-weight: 800; text-shadow: 1px 1px 1px rgba(0,0,0,0.35);
  }
  .headline .sm { display: block; font-size: 31px; line-height: 34px; }
  .headline .lg { display: block; font-size: 48px; line-height: 46px; }
  .headline-rule { position: absolute; left: 316px; top: 161px; width: 214px; height: 3px; background: var(--white); }
  .headline--second { top: 170px; }

  /* back */
  .back__panel { position: absolute; left: 206px; top: 0; width: 324px; height: 429px; background: var(--taupe-panel); }
  .ghost-ring { position: absolute; border-radius: 50%; border: 26px solid var(--ghost); }
  .ghost-ring--top { left: 330px; top: 40px; width: 240px; height: 240px; }
  .ghost-ring--bottom { left: 80px; top: 520px; width: 360px; height: 360px; }
  .brand-back { position: absolute; left: 30px; top: 30px; width: 160px; text-align: center; }
  .brand-back .brand-dot { width: 62px; height: 62px; margin-bottom: 16px; }
  .brand-back .brand-name { font-size: 20px; }
  .pricing { position: absolute; left: 31px; color: var(--ink-soft); font-weight: 700; }
  .pricing .label { display: block; font-size: 15px; line-height: 17px; }
  .pricing .value { display: block; font-size: 23px; line-height: 25px; }
  .pricing--month { top: 184px; }
  .pricing--day { top: 271px; }
  .pricing--none { top: 358px; font-size: 24px; line-height: 26px; }
  .call-top { position: absolute; left: 237px; top: 62px; color: var(--ink); font-weight: 700; font-size: 21px; }
  .benefits {
    position: absolute; left: 218px; top: 136px; width: 300px; list-style: none;
    color: var(--white); font-weight: 600; font-size: 14.5px; line-height: 18.7px;
  }
  .benefits li { position: relative; padding-left: 16px; }
  .benefits li::before { content: "•"; position: absolute; left: 2px; }
  .cta { position: absolute; left: 111px; top: 464px; display: flex; align-items: center; gap: 8px; }
  .cta__text { color: var(--ink); font-weight: 700; font-size: 17.5px; }
  .closing { position: absolute; left: 0; top: 571px; width: 530px; text-align: center; color: var(--ink-soft); font-weight: 700; }
  .closing .note { display: block; font-size: 15.5px; }
  .closing .phone { display: block; font-size: 22px; line-height: 26px; }
</style>
</head>
<body>
<main class="canvas">
  <section class="page page--front">
    <div class="front__left"></div>
    <div class="front__photo" role="img" aria-label="Photo of a designer in a plaid shirt and cap sketching a website wireframe on glass, with thought bubbles"></div>
    <h1 class="build-title">BUILD<br>YOUR<br>WEBSITE<small>WITH</small></h1>
    <div class="brand-front">
      <span class="brand-dot"></span>
      <span class="brand-name">Novaweb Studio</span>
    </div>
    <h2 class="headline"><span class="sm">ATTRACT</span><span class="lg">MORE</span><span class="sm">CUSTOMERS</span></h2>
    <div class="headline-rule"></div>
    <h2 class="headline headline--second"><span class="sm">MAKE</span><span class="lg">MORE</span><span class="sm">MONEY</span></h2>
  </section>

  <section class="page page--back">
    <div class="back__panel"></div>
    <div class="ghost-ring ghost-ring--top"></div>
    <div class="ghost-ring ghost-ring--bottom"></div>
    <div class="brand-back">
      <span class="brand-dot"></span>
      <span class="brand-name">Novaweb Studio</span>
    </div>
    <p class="pricing pricing--month"><span class="label">PRICING:</span><span class="value">ONLY $99.00</span><span class="label">PER MONTH</span></p>
    <p class="pricing pricing--day"><span class="label">THAT’S</span><span class="value">ONLY $3.30</span><span class="label">PER DAY</span></p>
    <p class="pricing pricing--none">NO OTHER<br>COSTS</p>
    <p class="call-top">Call Today: 1-800-555-0142</p>
    <ul class="benefits">
      <li>97% of people look online<br>for businesses. You need a website</li>
      <li>You’re losing many customers<br>by not having a website</li>
      <li>Beat your competition with better<br>visibility and credibility</li>
      <li>Beautiful Websites Available Now</li>
      <li>Smart, clean website designs<br>($3000 Value. No extra charge)</li>
      <li>Limited to ONLY 4 WEBSITES per area.<br>Don’t miss out!</li>
      <li>Social Media setup options<br>(Findora &amp; Circlebook)</li>
    </ul>
    <div class="cta">
      <svg width="86" height="60" viewBox="0 0 86 60" aria-hidden="true">
        <path d="M4 34 V4 H80 V34" fill="none" stroke="#4b4b4b" stroke-width="4"/>
        <path d="M4 30 V38 H48" fill="none" stroke="#4b4b4b" stroke-width="4"/>
        <text x="13" y="27" font-family="Source Sans 3, sans-serif" font-weight="700" font-size="17" fill="#4b4b4b">www.</text>
        <rect x="64" y="12" width="2.5" height="18" fill="#4b4b4b"/>
        <path d="M50 30 L70 44 L61 46 L66 56 L62 58 L57 48 L51 54 Z" fill="#4b4b4b" stroke="#eeeae1" stroke-width="1.5"/>
      </svg>
      <span class="cta__text">CREATE A WEBSITE TODAY!</span>
    </div>
    <p class="closing"><span class="note">Stop wasting money on mailers and print advertising.</span><span class="phone">CALL: 1-800-555-0142</span></p>
  </section>
</main>
</body>
</html>
```